Trade Show Poster/Booth Backdrop for Rugged Technology Business

I need a graphic design for an 8' x 6' poster to hang on back wall of my event booth. Design must be consistent with my company's colors, logo, and current branding as shown on website, Facebook, and Twitter (links provided). You can propose other elements, but there are certain core images and text elements that must be incorporated. Print specifications also provided. File must be delivered on time and upload-ready.

Font styles to use
Sans Serif

Colors
33a6d7
0355a3
33b8a4
00a990
9bcb3b
abd036
cadf82
85cae6
86cfc6

Requirements
Nice to have
• Regarding color, I'm okay with designs using the orange version of the Morvex logo.
• Regarding the images I provided as potential background layers, I especially like the ones with rocky island profiles and exposed cliff faces. In addition to being a nice match color wise, they are subtle suggestions of ruggedness and working with technology that can handle extreme environments (which is a big part of the messaging focus).
Should not have
• Vibrant coloration is very much desired and OK, but please avoid a blend that goes to either extreme. For instance, too much dark blue makes it look like every other tech company ever. Too much warm, light green (other than for contrast elements) makes it look too tropical and casual.

```html
<!DOCTYPE html>
<html lang="en">
<head>
<meta charset="utf-8">
<title>Solenne Enterprises – Rugged &amp; Business Class Technology</title>
<link rel="stylesheet" href="https://fonts.googleapis.com/css2?family=Lato:wght@300;400;700&display=swap">
<style>
  :root {
    --deep-blue: #0a4fa6;
    --mid-blue: #1478b4;
    --teal: #12967a;
    --green: #1a9a48;
    --sea-light: #6fb7c4;
    --white: #ffffff;
    --white-soft: rgba(255,255,255,0.85);
  }
  * { margin: 0; padding: 0; box-sizing: border-box; }
  html, body { width: 901px; height: 1200px; overflow: hidden; background: #fff; }
  .poster {
    position: relative;
    width: 901px;
    height: 1200px;
    overflow: hidden;
    font-family: "Lato", "Helvetica Neue", Arial, sans-serif;
    color: var(--white);
    background: linear-gradient(100deg, var(--deep-blue) 0%, var(--mid-blue) 30%, var(--teal) 65%, var(--green) 100%);
  }
  .backdrop-scene {
    position: absolute;
    left: 0; right: 0;
    top: 560px; bottom: 0;
    background:
      linear-gradient(180deg, rgba(111,183,196,0) 0%, rgba(111,183,196,0.28) 18%, rgba(111,183,196,0.12) 55%, rgba(10,79,166,0) 100%),
      radial-gradient(ellipse 220px 70px at 40px 330px, rgba(40,80,110,0.45), rgba(40,80,110,0) 100%);
  }
  .brand-row {
    position: absolute;
    top: 100px;
    left: 103px;
    display: flex;
    align-items: center;
    gap: 58px;
  }
  .brand {
    display: flex;
    align-items: center;
    gap: 12px;
    font-weight: 700;
    font-size: 30px;
    letter-spacing: 0.04em;
    color: var(--white);
  }
  .brand-mark {
    width: 62px; height: 62px;
    border-radius: 50%;
    background: var(--white);
  }
  .brand-lead { letter-spacing: 0.12em; }
  .headline {
    position: absolute;
    top: 222px;
    left: 101px;
    font-weight: 300;
    font-size: 66px;
    line-height: 77px;
    letter-spacing: 0.055em;
    text-transform: uppercase;
  }
  .offerings {
    position: absolute;
    top: 578px;
    left: 103px;
    list-style: none;
    font-weight: 300;
    font-size: 34px;
    letter-spacing: 0.03em;
  }
  .offerings li { height: 66px; line-height: 44px; position: relative; }
  .offerings li + li::before {
    content: "";
    position: absolute;
    top: -10px;
    left: 2px;
    width: 30px;
    height: 2px;
    background: var(--white-soft);
  }
  .contact-bar {
    position: absolute;
    top: 1083px;
    left: 103px;
    display: flex;
    align-items: center;
    font-size: 21px;
    font-weight: 400;
  }
  .contact-item { display: flex; align-items: center; gap: 12px; }
  .contact-item + .contact-item { margin-left: 58px; }
  .contact-marker {
    width: 24px; height: 24px;
    background: var(--white);
    border-radius: 3px;
  }
  .contact-marker.round { border-radius: 50%; }
</style>
</head>
<body>
  <main class="poster">
    <div class="backdrop-scene" role="img" aria-label="Calm ocean shoreline with a low rocky outcrop, tinted in blue and green"></div>

    <header class="brand-row">
      <div class="brand brand-lead"><span class="brand-mark"></span>SOLENNE</div>
      <div class="brand">Morvex</div>
      <div class="brand">Corvane</div>
    </header>

    <h1 class="headline">Fully Rugged &amp;<br>Business Class<br>Technology<br>Solutions</h1>

    <ul class="offerings">
      <li>Mobility</li>
      <li>Computing</li>
      <li>Mounting</li>
      <li>Printing</li>
      <li>Imaging</li>
      <li>Storage</li>
    </ul>

    <footer class="contact-bar">
      <div class="contact-item"><span class="contact-marker"></span>SolenneforIT</div>
      <div class="contact-item"><span class="contact-marker"></span>SolenneforIT</div>
      <div class="contact-item"><span class="contact-marker round"></span>solenneenterprises.net</div>
    </footer>
  </main>
</body>
</html>
```